Online Marketing Agency Website

We are an online marketing agency that specializes in search marketing (SEM) for businesses of all sizes. Our core services include local search marketing, seo, paid search, paid social, graphic design, video production/editing and website design. We have an existing website that we launched a number of years ago but it's very outdated and we're currently too busy to design a new version.

Target Market(s)

Any business that needs online marketing services with an emphasis on search marketing.

Industry/Entity Type

Ad Agency

Number of Pages Required

4 page

Font styles to use
Sans Serif

Requirements
Must have
• Home page, interior page, blog page, contact us page.
Look and feel should be modern and clean and easy to navigate.
Sections for call outs for specific services: Business Marketing Strategy, Content Creation and Marketing, Graphic & Publication Design, Pay Per Click (PPC) Management, Search Engine Optimization, Social Media Management, Video Production & Editing, Website Hosting & Management, Website Design & Development
Use color from logo that was uploaded.

```html
<!DOCTYPE html>
<html lang="en">
<head>
<meta charset="utf-8">
<title>Nova Reach — Online Marketing Agency</title>
<link href="https://fonts.googleapis.com/css2?family=Poppins:ital,wght@0,300;0,400;0,500;0,600;0,700;1,400&display=swap" rel="stylesheet">
<style>
:root{
  --orange:#fc4a0e;
  --orange-soft:#fde3d9;
  --ink:#2b2b2b;
  --text:#6d6d6d;
  --light:#f7f7f7;
  --dark:#151515;
  --white:#ffffff;
}
*{box-sizing:border-box;margin:0;padding:0}
html,body{width:1200px;height:3246px;overflow:hidden}
body{font-family:'Poppins',sans-serif;color:var(--ink);background:var(--white);position:relative}
a{color:inherit;text-decoration:none}

/* hero */
.hero{position:absolute;left:0;top:0;width:1200px;height:556px;overflow:hidden;background:var(--white)}
.hero-bg{position:absolute;left:-300px;top:-500px;width:1150px;height:1056px;background:var(--light);border-radius:0 0 480px 0}
.hero-photo{position:absolute;left:523px;top:-330px;width:880px;height:880px;border-radius:50%;border:2px solid var(--orange);background:linear-gradient(135deg,#d9d4cf 0%,#b9b3ad 35%,#e8e5e2 60%,#8d8780 100%)}
.brand{position:absolute;display:flex;align-items:center;gap:8px;font-weight:600;color:var(--ink)}
.brand-dot{width:12px;height:12px;border-radius:50%;background:var(--orange)}
.hero .brand{left:82px;top:42px;font-size:14px}
.nav{position:absolute;top:24px;left:774px;font-size:13px;color:var(--white)}
.nav a{position:absolute;white-space:nowrap}
.signin{position:absolute;left:266px;top:-6px;width:74px;height:32px;border:1px solid var(--white);border-radius:16px;font-size:10px;font-weight:600;letter-spacing:1px;display:flex;align-items:center;justify-content:center}
.hero-title{position:absolute;left:82px;top:162px;font-size:42px;font-weight:300;line-height:42px;color:var(--ink)}
.hero-title strong{display:block;font-weight:600;font-size:40px;margin-top:8px}
.hero-text{position:absolute;left:82px;top:308px;width:410px;font-size:12px;line-height:20px;color:var(--text)}
.btn{position:absolute;display:flex;align-items:center;justify-content:center;background:var(--orange);color:var(--white);font-size:11px;font-weight:600;letter-spacing:.6px;border-radius:20px;box-shadow:0 6px 14px rgba(252,74,14,.25)}

/* services */
.section-title{position:absolute;left:0;width:1200px;text-align:center;font-weight:500;font-size:35px;color:var(--ink)}
.service{position:absolute;width:300px}
.service-icon{width:46px;height:46px;border-radius:50%;background:var(--orange-soft);display:flex;align-items:center;justify-content:center}
.service h3{font-size:17px;font-weight:500;margin-top:14px;color:var(--ink)}
.service p{font-size:11.5px;line-height:19px;color:var(--text);margin-top:10px}
.read-more{display:flex;align-items:center;gap:8px;margin-top:14px;font-size:11.5px;color:var(--orange)}

/* about */
.about-photo{position:absolute;left:0;top:1294px;width:554px;height:468px;border-radius:0 260px 260px 0;border:2px solid var(--orange);border-left:none;background:linear-gradient(120deg,#2d3a50 0%,#55647c 45%,#8e9bb0 75%,#3b4558 100%)}
.about-title{position:absolute;left:638px;top:1386px;font-size:35px;font-weight:600}
.about-text{position:absolute;left:638px;top:1450px;width:470px;font-size:13.5px;line-height:25px;color:var(--text)}
.stat{position:absolute;top:1572px}
.stat b{display:block;font-size:25px;font-weight:600;color:var(--orange)}
.stat span{font-size:12.5px;color:var(--text)}
.stat-sep{position:absolute;top:1578px;width:1px;height:42px;background:#e4e4e4}

/* testimonials */
.quote-card{position:absolute;top:1991px;height:186px;background:var(--white);box-shadow:0 8px 30px rgba(0,0,0,.06)}
.quote-card p{position:absolute;top:66px;font-size:14px;font-style:italic;line-height:25px;color:#9a9a9a;white-space:nowrap}
.quote-mark{position:absolute;top:20px;font-size:110px;line-height:110px;font-weight:700;color:var(--orange-soft)}
.quote-tail{position:absolute;top:2177px;width:0;height:0;border-left:14px solid transparent;border-right:14px solid transparent;border-top:22px solid var(--white)}
.avatar{position:absolute;top:2236px;width:90px;height:90px;border-radius:50%;background:linear-gradient(160deg,#d6d0ca,#8e8882);border:5px solid var(--white);box-shadow:0 6px 20px rgba(0,0,0,.1)}
.person{position:absolute;top:2262px}
.person b{display:block;font-size:17px;font-weight:500;color:var(--ink)}
.person span{font-size:12.5px;color:#9a9a9a}

/* contact */
.dark-band{position:absolute;left:0;top:2631px;width:1200px;height:615px;background:var(--dark)}
.form-panel{position:absolute;left:82px;top:2385px;width:654px;height:523px;background:var(--orange);color:var(--white)}
.panel-title{position:absolute;left:48px;top:48px;font-size:26px;font-weight:600}
.panel-rule{position:absolute;left:50px;top:86px;width:28px;height:2px}
.field{position:absolute;border-bottom:1px solid rgba(255,255,255,.35);font-size:11px;letter-spacing:.4px;padding-bottom:30px;color:rgba(255,255,255,.9)}
.submit{position:absolute;left:456px;top:427px;width:116px;height:38px;border-radius:20px;background:var(--white);color:var(--ink);font-size:11px;font-weight:600;letter-spacing:1px;display:flex;align-items:center;justify-content:center}
.info-panel{position:absolute;left:736px;top:2385px;width:380px;height:523px;background:var(--white)}
.info-panel .panel-title{color:var(--ink)}
.info-label{position:absolute;left:78px;display:flex;align-items:center;gap:12px;font-size:11.5px;letter-spacing:.6px;color:var(--text)}
.info-label svg{position:absolute;left:-30px}
.info-value{position:absolute;left:78px;font-size:13.5px;font-weight:500;line-height:22px;color:var(--ink)}

/* footer */
.footer-head{position:absolute;top:3030px;font-size:11.5px;letter-spacing:.6px;color:#bdbdbd}
.footer-link{position:absolute;font-size:13px;color:var(--white)}
.social{position:absolute;top:3066px;width:12px;height:12px;border-radius:50%;border:1.5px solid var(--white)}
.newsletter{position:absolute;left:825px;top:3062px;width:290px;height:40px;border-radius:20px;background:#252525;font-size:11px;color:#c9c9c9;display:flex;align-items:center;padding-left:18px}
.newsletter svg{position:absolute;right:16px;top:11px}
.footer-rule{position:absolute;left:0;top:3190px;width:1200px;height:1px;background:#2a2a2a}
.legal{position:absolute;top:3212px;font-size:11px;color:#d4d4d4}
</style>
</head>
<body>

<header class="hero">
  <div class="hero-bg"></div>
  <div class="hero-photo" role="img" aria-label="Photo of a team working on laptops around a meeting table"></div>
  <div class="brand"><span class="brand-dot"></span>NOVA REACH</div>
  <nav class="nav">
    <a style="left:0">Home</a>
    <a style="left:69px">About</a>
    <a style="left:137px">Blog</a>
    <a style="left:194px">Contact</a>
    <a class="signin">SIGN IN</a>
  </nav>
  <h1 class="hero-title">Nova Reach is a<br>full-service online<strong>MARKETING AGENCY</strong></h1>
  <p class="hero-text">We can handle any element of your online marketing so you can get back to doing what you do best — growing your business. All of our services are offered on an ‘a la carte’ basis.</p>
  <a class="btn" style="left:83px;top:398px;width:174px;height:37px">EXPLORE OUR SERVICES</a>
</header>

<h2 class="section-title" style="top:634px">Our Services</h2>

<section class="services">
  <div class="service" style="left:82px;top:714px">
    <div class="service-icon"><svg width="20" height="20" viewBox="0 0 20 20"><circle cx="10" cy="10" r="4" fill="none" stroke="#fc4a0e" stroke-width="1.5"/><path d="M10 1v3M10 16v3M1 10h3M16 10h3M3.5 3.5l2 2M14.5 14.5l2 2M3.5 16.5l2-2M14.5 5.5l2-2" stroke="#fc4a0e" stroke-width="1.5"/></svg></div>
    <h3>Business Marketing Strategy</h3>
    <p>Let us strategize the big picture for you. With decades of experience, we have...</p>
    <a class="read-more">Read More <svg width="16" height="8" viewBox="0 0 16 8"><path d="M0 4h14M11 1l3 3-3 3" fill="none" stroke="#fc4a0e"/></svg></a>
  </div>
  <div class="service" style="left:454px;top:714px">
    <div class="service-icon"><svg width="20" height="20" viewBox="0 0 20 20"><rect x="3" y="3" width="14" height="14" rx="1" fill="none" stroke="#fc4a0e" stroke-width="1.5"/><path d="M6 7h8M6 10h4M6 13h4M12 10h2v3h-2z" stroke="#fc4a0e" stroke-width="1.3" fill="none"/></svg></div>
    <h3>Content Creation &amp; Marketing</h3>
    <p>You’ve heard it before. “Content is king.” Search engines love it and customers expect it.</p>
    <a class="read-more">Read More <svg width="16" height="8" viewBox="0 0 16 8"><path d="M0 4h14M11 1l3 3-3 3" fill="none" stroke="#fc4a0e"/></svg></a>
  </div>
  <div class="service" style="left:830px;top:714px">
    <div class="service-icon"><svg width="20" height="20" viewBox="0 0 20 20"><path d="M10 3l5 7-5 7-5-7z" fill="none" stroke="#fc4a0e" stroke-width="1.5"/><circle cx="10" cy="10" r="1.6" fill="#fc4a0e"/></svg></div>
    <h3>Graphic &amp; Publication Design</h3>
    <p>Our designers have decades of experience in everything from tradeshow graphics...</p>
    <a class="read-more">Read More <svg width="16" height="8" viewBox="0 0 16 8"><path d="M0 4h14M11 1l3 3-3 3" fill="none" stroke="#fc4a0e"/></svg></a>
  </div>
  <div class="service" style="left:82px;top:938px">
    <div class="service-icon"><svg width="20" height="20" viewBox="0 0 20 20"><circle cx="10" cy="9" r="2" fill="#fc4a0e"/><path d="M10 11v7M6 5a6 6 0 000 8M14 5a6 6 0 010 8M3.5 3a9 9 0 000 12M16.5 3a9 9 0 010 12" fill="none" stroke="#fc4a0e" stroke-width="1.4"/></svg></div>
    <h3>Pay Per Click (PPC) Management</h3>
    <p>PPC advertising delivers some of the best ROI online...but it can be overwhelming.</p>
    <a class="read-more">Read More <svg width="16" height="8" viewBox="0 0 16 8"><path d="M0 4h14M11 1l3 3-3 3" fill="none" stroke="#fc4a0e"/></svg></a>
  </div>
  <div class="service" style="left:454px;top:938px">
    <div class="service-icon"><svg width="20" height="20" viewBox="0 0 20 20"><circle cx="12" cy="8" r="5" fill="none" stroke="#fc4a0e" stroke-width="1.5"/><path d="M8.5 11.5L3 17" stroke="#fc4a0e" stroke-width="2"/></svg></div>
    <h3>Search Engine Optimization</h3>
    <p>The SEO playing field is shifting constantly. From week to week, the rules change...</p>
    <a class="read-more">Read More <svg width="16" height="8" viewBox="0 0 16 8"><path d="M0 4h14M11 1l3 3-3 3" fill="none" stroke="#fc4a0e"/></svg></a>
  </div>
  <div class="service" style="left:830px;top:938px">
    <div class="service-icon"><svg width="20" height="20" viewBox="0 0 20 20"><rect x="3" y="5" width="14" height="9" rx="1" fill="none" stroke="#fc4a0e" stroke-width="1.5"/><path d="M7 17h6M10 14v3" stroke="#fc4a0e" stroke-width="1.5"/></svg></div>
    <h3>Social Media Management</h3>
    <p>Scratching your head over how to make social media work for you?</p>
    <a class="read-more">Read More <svg width="16" height="8" viewBox="0 0 16 8"><path d="M0 4h14M11 1l3 3-3 3" fill="none" stroke="#fc4a0e"/></svg></a>
  </div>
</section>

<a class="btn" style="left:518px;top:1191px;width:164px;height:35px">OUR ALL SERVICES</a>

<section class="about">
  <div class="about-photo" role="img" aria-label="Photo of a hand holding a tablet with a digital marketing network graphic"></div>
  <h2 class="about-title">About Us</h2>
  <p class="about-text">Mauris at eros vel turpis congue placerat. Vivamus ac semper justo, vitae aliquam neque. Sed varius facilisis scelerisque. Praesent laoreet eros eu quam laoreet pellentesque. Sed malesuada arcu ac nulla eleifend, vel varius ligula dictum.</p>
  <div class="stat" style="left:639px"><b>200</b><span>Projects Done</span></div>
  <div class="stat-sep" style="left:758px"></div>
  <div class="stat" style="left:784px"><b>250</b><span>Consultants</span></div>
  <div class="stat-sep" style="left:890px"></div>
  <div class="stat" style="left:917px"><b>150</b><span>Awards</span></div>
  <div class="stat-sep" style="left:995px"></div>
  <div class="stat" style="left:1027px"><b>170</b><span>Happy Clients</span></div>
  <a class="btn" style="left:639px;top:1667px;width:130px;height:36px">LEARN MORE</a>
</section>

<h2 class="section-title" style="top:1876px">What People Say about Us</h2>

<section class="testimonials">
  <div class="quote-card" style="left:-430px;width:647px;overflow:hidden">
    <p style="left:54px">Pellentesque eget iaculis massa, in ultrices libero. Nullam interdum sem mauris,<br>cursus risus consectetur nec. Praesent non elit faucibus sem maximus porta.<br>Nullam dictum orci id pretium aliquam. Integer massa turpis.</p>
  </div>
  <div class="quote-card" style="left:272px;width:640px">
    <span class="quote-mark" style="left:44px">“</span>
    <p style="left:54px">Pellentesque eget iaculis massa, in ultrices libero. Nullam interdum sem mauris,<br>cursus risus consectetur nec. Praesent non elit faucibus sem maximus porta.<br>Nullam dictum orci id pretium aliquam. Integer massa turpis.</p>
  </div>
  <div class="quote-tail" style="left:322px"></div>
  <div class="quote-card" style="left:977px;width:223px;overflow:hidden">
    <span class="quote-mark" style="left:44px">“</span>
    <p style="left:54px">Pellentesque eget iaculis massa, in ultrices libero.<br>cursus risus consectetur nec. Praesent non elit.<br>Nullam dictum orci id pretium aliquam.</p>
  </div>
  <div class="quote-tail" style="left:1027px"></div>

  <div class="avatar" style="left:276px" role="img" aria-label="Portrait photo of a client"></div>
  <div class="person" style="left:394px"><b>Daniel Moore</b><span>CTO @ Brightpath</span></div>
  <div class="avatar" style="left:983px" role="img" aria-label="Portrait photo of a client"></div>
  <div class="person" style="left:1097px;white-space:nowrap"><b>Liam Carter</b><span>CEO @ Northgrid</span></div>
</section>

<div class="dark-band"></div>

<section class="contact">
  <form class="form-panel">
    <h2 class="panel-title">Fill The Form Below</h2>
    <div class="panel-rule" style="background:var(--white)"></div>
    <div class="field" style="left:41px;top:133px;width:245px;padding-left:8px">FIRST NAME</div>
    <div class="field" style="left:328px;top:133px;width:244px;padding-left:8px">LAST NAME</div>
    <div class="field" style="left:41px;top:237px;width:245px;padding-left:8px">PHONE</div>
    <div class="field" style="left:328px;top:237px;width:244px;padding-left:8px">EMAIL ADDRESS</div>
    <div class="field" style="left:41px;top:323px;width:531px;padding-left:8px;padding-bottom:60px">MESSAGE</div>
    <div class="submit">SUBMIT</div>
  </form>

  <div class="info-panel">
    <h2 class="panel-title">Contact Us</h2>
    <div class="panel-rule" style="background:var(--ink)"></div>
    <div class="info-label" style="top:138px"><svg width="14" height="18" viewBox="0 0 14 18"><path d="M7 1a6 6 0 016 6c0 4.5-6 10-6 10S1 11.5 1 7a6 6 0 016-6z" fill="#fc4a0e"/><circle cx="7" cy="7" r="2.2" fill="#fff"/></svg>LOCATION</div>
    <div class="info-value" style="top:166px">Lindenhof Street 12, Am Kanal<br>8 Road by 10115 Berlin</div>
    <div class="info-label" style="top:273px"><svg width="16" height="16" viewBox="0 0 16 16"><path d="M3 1l3 3-1.5 2.5a9 9 0 005 5L12 10l3 3-2 2C7 15 1 9 1 3z" fill="#fc4a0e"/></svg>CALL</div>
    <div class="info-value" style="top:300px;font-size:21px">0123 456 7890</div>
    <div class="info-label" style="top:384px"><svg width="16" height="12" viewBox="0 0 16 12"><rect width="16" height="12" rx="1" fill="#fc4a0e"/><path d="M1 1l7 6 7-6" fill="none" stroke="#fff" stroke-width="1.3"/></svg>EMAIL ADDRESS</div>
    <div class="info-value" style="top:414px">hello@novareach.com</div>
  </div>
</section>

<footer>
  <div class="brand" style="left:84px;top:3092px;color:var(--white);font-size:18px"><span class="brand-dot"></span>NOVA REACH</div>
  <div class="footer-head" style="left:392px">QUICK LINKS:</div>
  <a class="footer-link" style="left:395px;top:3070px">Home</a>
  <a class="footer-link" style="left:462px;top:3070px">About</a>
  <a class="footer-link" style="left:395px;top:3103px">Blog</a>
  <a class="footer-link" style="left:462px;top:3103px">Contact</a>
  <div class="footer-head" style="left:629px">FOLLOW US:</div>
  <span class="social" style="left:627px"></span>
  <span class="social" style="left:655px"></span>
  <span class="social" style="left:685px"></span>
  <span class="social" style="left:715px"></span>
  <div class="footer-head" style="left:828px">NEWSLETTERS:</div>
  <div class="newsletter">Enter Your Email
    <svg width="22" height="18" viewBox="0 0 22 18"><path d="M1 8l20-7-6 16-4-6z M11 11l10-10" fill="none" stroke="#fc4a0e" stroke-width="1.5" stroke-linejoin="round"/></svg>
  </div>
  <div class="footer-rule"></div>
  <div class="legal" style="left:84px">© 2020 Nova Reach. All Right Reserved.</div>
  <div class="legal" style="left:911px">Terms &amp; Conditions</div>
  <div class="legal" style="left:1044px">Privacy Policy</div>
</footer>

</body>
</html>
```